KORVELTA Corporate Business Card

Modern business card design for company which focuses in the areas of Staffing, IT Consulting & Data Services. Please note: We are no longer using the IT subscript on the logo. All designs should have IT subscript removed.
Website: www.korveltait.example

```html
<!DOCTYPE html>
<html lang="en">
<head>
<meta charset="utf-8">
<title>KORVELTA Business Card</title>
<link href="https://fonts.googleapis.com/css2?family=Open+Sans:wght@400;600;700&display=swap" rel="stylesheet">
<style>
  :root {
    --page-bg: #ececec;
    --card-white: #ffffff;
    --brand-blue: #1e9bd7;
    --deep-blue: #055b96;
    --text-grey: #6b6b6b;
    --icon-blue: #1a5f95;
  }
  * { margin: 0; padding: 0; box-sizing: border-box; }
  html, body {
    width: 1125px; height: 1200px; overflow: hidden;
    background: var(--page-bg);
    font-family: "Open Sans", Arial, sans-serif;
  }
  .card {
    position: absolute;
    left: 104px;
    width: 916px; height: 520px;
    border-radius: 29px;
    overflow: hidden;
  }
  .card-front { top: 55px; background: var(--card-white); }
  .card-back { top: 625px; background: var(--deep-blue); }

  .brand-mark {
    position: absolute; left: 86px; top: 225px;
    display: flex; align-items: center; gap: 14px;
  }
  .brand-square {
    width: 34px; height: 34px; background: var(--brand-blue);
  }
  .brand-name {
    font-size: 56px; font-weight: 600; line-height: 1;
    color: var(--brand-blue); letter-spacing: 1px;
  }
  .divider {
    position: absolute; left: 457px; top: 145px;
    width: 2px; height: 230px; background: var(--brand-blue);
  }
  .contact-block {
    position: absolute; left: 494px; top: 143px;
    color: var(--text-grey);
  }
  .person-name {
    font-size: 29px; font-weight: 600; color: var(--brand-blue);
    line-height: 38px; letter-spacing: 0.5px;
  }
  .person-title { font-size: 21px; line-height: 26px; }
  .contact-list { list-style: none; margin-top: 12px; }
  .contact-list li {
    display: flex; align-items: center; gap: 8px;
    font-size: 21px; line-height: 31.5px;
  }
  .contact-list svg { width: 12px; height: 12px; flex: none; }
  .address { margin-top: 10px; font-size: 21px; line-height: 26px; }

  .back-name {
    position: absolute; left: 61px; top: 352px;
    font-size: 84px; font-weight: 700; line-height: 1;
    color: var(--card-white); letter-spacing: 1px;
  }
</style>
</head>
<body>
  <section class="card card-front">
    <div class="brand-mark">
      <span class="brand-square"></span>
      <span class="brand-name">KORVELTA</span>
    </div>
    <div class="divider"></div>
    <div class="contact-block">
      <div class="person-name">DALIA VORENSK</div>
      <div class="person-title">Manager</div>
      <ul class="contact-list">
        <li>
          <svg viewBox="0 0 12 12" aria-hidden="true"><rect x="3" y="0.5" width="6" height="11" rx="1" fill="none" stroke="var(--icon-blue)" stroke-width="1.4"/><circle cx="6" cy="9.3" r="0.9" fill="var(--icon-blue)"/></svg>
          555-014-2290
        </li>
        <li>
          <svg viewBox="0 0 12 12" aria-hidden="true"><rect x="0.7" y="2.5" width="10.6" height="7" fill="none" stroke="var(--icon-blue)" stroke-width="1"/><path d="M0.7 2.5 L6 6.5 L11.3 2.5" fill="none" stroke="var(--icon-blue)" stroke-width="1"/></svg>
          contactus@korveltait.example
        </li>
        <li>
          <svg viewBox="0 0 12 12" aria-hidden="true"><circle cx="6" cy="6" r="5" fill="none" stroke="var(--icon-blue)" stroke-width="1.2"/><ellipse cx="6" cy="6" rx="2.2" ry="5" fill="none" stroke="var(--icon-blue)" stroke-width="1"/><path d="M1 6 H11 M2 3.5 H10 M2 8.5 H10" stroke="var(--icon-blue)" stroke-width="0.9"/></svg>
          www.korveltait.example
        </li>
      </ul>
      <div class="address">418 Larkmoor Ave.<br>Calderwick, IN 47199</div>
    </div>
  </section>

  <section class="card card-back">
    <div class="back-name">KORVELTA</div>
  </section>
</body>
</html>
```